Torvel, Inc. new buisness cards - brand guide included

We need new business cards. SLEAK SIMPLE FINANCE. They must include a place for NAME, TITLE, CELL, OFFICE PHONE, EMAIL. they also must include our services across the bottom. AIR, OCEAN, FTL, LTL, EXPRESS. for reference this will be being handed to some of the most prestigious shipping companies in a america.

Target Market(s)

Finance and corporate

Contact Information for Business Card

We need new business cards. SLEAK SIMPLE FINANCE. They must include a place for NAME, TITLE, CELL, OFFICE PHONE, EMAIL. they also must include our services across the bottom. AIR, OCEAN, FTL, LTL, EXPRESS.

Requirements
Must have
• We need new business cards. SLEAK SIMPLE FINANCE. They must include a place for NAME, TITLE, CELL, OFFICE PHONE, EMAIL. they also must include our services across the bottom. AIR, OCEAN, FTL, LTL, EXPRESS.
Nice to have
• USE THE COLORS AND LOGO IN THE BRAND GUIDE :)

```html
<!DOCTYPE html>
<html lang="en">
<head>
<meta charset="utf-8">
<title>Torvel, Inc. — Business Card</title>
<link href="https://fonts.googleapis.com/css2?family=Montserrat:wght@400;700&display=swap" rel="stylesheet">
<style>
  :root {
    --backdrop: #141414;
    --card: #232323;
    --ink: #f4f2ee;
    --rule: #d9d6d0;
  }
  * { margin: 0; padding: 0; box-sizing: border-box; }
  html, body { width: 1200px; height: 900px; overflow: hidden; background: var(--backdrop); }
  body { position: relative; font-family: 'Montserrat', sans-serif; color: var(--ink); }

  .card {
    position: absolute; left: 300px; width: 600px; height: 343px;
    background: var(--card); border-radius: 18px; overflow: hidden;
  }
  .card--front { top: 60px; }
  .card--back { top: 470px; }

  /* Front */
  .brand-name {
    position: absolute; left: 0; right: 0; top: 118px;
    text-align: center; font-weight: 400; font-size: 52px; letter-spacing: 10px;
  }
  .services {
    position: absolute; left: 0; right: 0; bottom: 48px;
    text-align: center; font-size: 14px; letter-spacing: 1.5px;
  }
  .services .dot { margin: 0 8px; }

  /* Back */
  .card--back .brand-name {
    left: auto; right: 44px; top: 46px; text-align: right; font-size: 38px; letter-spacing: 7px;
  }
  .edge-tab {
    position: absolute; left: 0; top: 202px; width: 14px; height: 34px;
    background: var(--ink); border-radius: 0 4px 4px 0;
  }
  .holder { position: absolute; left: 44px; top: 196px; }
  .holder-name { font-weight: 700; font-size: 18px; letter-spacing: 1px; }
  .holder-title { font-size: 13px; margin-top: 2px; }
  .rule { position: absolute; left: 44px; right: 24px; height: 1px; background: var(--rule); }
  .rule--top { top: 182px; left: 250px; right: 44px; }
  .rule--mid { top: 250px; }
  .rule--low { top: 294px; right: 44px; }
  .contact-row {
    position: absolute; left: 44px; right: 20px; top: 262px;
    display: flex; gap: 14px; font-size: 12.5px; white-space: nowrap;
  }
  .contact-item { display: flex; align-items: center; gap: 5px; }
  .contact-item svg { width: 11px; height: 11px; fill: none; stroke: var(--ink); stroke-width: 1.6; }
  .address { position: absolute; left: 44px; top: 306px; font-size: 13px; }
</style>
</head>
<body>
  <section class="card card--front">
    <div class="brand-name">TORVEL</div>
    <div class="services">Air<span class="dot">•</span>Ocean<span class="dot">•</span>Ftl<span class="dot">•</span>Ltl<span class="dot">•</span>Express</div>
  </section>

  <section class="card card--back">
    <div class="brand-name">TORVEL</div>
    <div class="rule rule--top"></div>
    <div class="edge-tab"></div>
    <div class="holder">
      <div class="holder-name">DORIAN HALE</div>
      <div class="holder-title">Founder/CEO</div>
    </div>
    <div class="rule rule--mid"></div>
    <div class="contact-row">
      <span class="contact-item">
        <svg viewBox="0 0 12 12"><path d="M2 1.5l2 .3.6 2.2-1.2 1a6 6 0 0 0 3.6 3.6l1-1.2 2.2.6.3 2c-5 .6-9-3.4-8.5-8.5z"/></svg>
        555.214.7730</span>
      <span class="contact-item">
        <svg viewBox="0 0 12 12"><rect x="3" y="1" width="6" height="10" rx="1"/><path d="M5.5 9h1"/></svg>
        555.214.8841</span>
      <span class="contact-item">
        <svg viewBox="0 0 12 12"><rect x="1" y="2.5" width="10" height="7"/><path d="M1 2.5l5 4 5-4"/></svg>
        info@torvelinc.com</span>
      <span class="contact-item">
        <svg viewBox="0 0 12 12"><circle cx="6" cy="6" r="5"/><path d="M1 6h10M6 1c-2.5 3-2.5 7 0 10M6 1c2.5 3 2.5 7 0 10"/></svg>
        www.torvelinc.com</span>
    </div>
    <div class="rule rule--low"></div>
    <div class="address">214 B. Harlow Drive Westbrook, KT 4102</div>
  </section>
</body>
</html>
```